Brightwell Ledger needs a Business Card

Designers!
More often than not, people want a cheap business card and often argue "I only want 100, not 500" - Years ago I worked in print and always wanted a client to ask for something that challenged me and would be great for my portfolio.

Years have past, and I dont have the time to do it myself so I'd love to see what everyone can offer.

Reason: Hey Guys, The designs are looking good but i've extended it a few more days as I wont be near a laptop and i'm trying to provide everyone feedback - Sorry!

Target Market(s)

Key decision makers, Potential Clients, Networking events and opportunities.

Industry/Entity Type

Business

Requirements
Must have
• Typography is very important. The type of paper is important.
The print, the shape. The creativity.
I'm very inspired by the below link
http://www.pelvarno.com/blog/business-card-design/

Nice to have
• Stencelled cutouts. Embossing, nice typography.
I'd like the business card to be a conversation piece itself.

Attached is an image of business cards i've had in the past.
Additionally, some logos i've recently had designed by MakerFlock.

```html
<!DOCTYPE html>
<html lang="en">
<head>
<meta charset="utf-8">
<title>Brightwell Ledger – Business Card</title>
<link rel="stylesheet" href="https://fonts.googleapis.com/css2?family=Advent+Pro:wght@200;300;400&family=Exo+2:wght@400;500&display=swap">
<style>
  :root {
    --backdrop: #b8c6b1;
    --card-border: #57ee1f;
    --card-stock: #eeefee;
    --ink-navy: #1b2a98;
    --rule-green: #62e82c;
  }
  html, body {
    margin: 0;
    width: 1200px;
    height: 900px;
    overflow: hidden;
    background: var(--backdrop);
  }
  .stage {
    position: relative;
    width: 1200px;
    height: 900px;
    font-family: "Exo 2", sans-serif;
    color: var(--ink-navy);
  }
  .card-shapes {
    position: absolute;
    inset: 0;
  }
  .text {
    position: absolute;
    margin: 0;
    white-space: nowrap;
    line-height: 1;
  }

  /* Back of card: brand */
  .brand-name {
    left: 262px; top: 560px;
    font-size: 31px;
    font-weight: 500;
    letter-spacing: 0.5px;
  }
  .brand-url {
    left: 256px; top: 620px;
    width: 286px;
    text-align: center;
    font-size: 13px;
    letter-spacing: 3.6px;
    color: var(--rule-green);
  }

  /* Front of card: contact */
  .person-name {
    left: 736px; top: 171px;
    font-size: 24px;
    font-weight: 500;
    letter-spacing: 2.6px;
  }
  .person-role {
    left: 733px; top: 207px;
    font-size: 26px;
    font-weight: 400;
  }
  .phone-number {
    left: 788px; top: 372px;
    font-family: "Advent Pro", sans-serif;
    font-weight: 200;
    font-size: 48px;
    letter-spacing: 0.5px;
    transform: scaleY(1.18);
    transform-origin: left top;
  }
  .website {
    left: 776px; top: 447px;
    font-size: 17px;
  }
  .social-handle {
    left: 793px; top: 491px;
    font-size: 20px;
    letter-spacing: 3.4px;
  }
  .email {
    left: 735px; top: 541px;
    font-family: "Advent Pro", sans-serif;
    font-weight: 300;
    font-size: 19px;
    letter-spacing: 1.2px;
    text-transform: uppercase;
  }
  .address-line {
    font-size: 17px;
    letter-spacing: 0.8px;
    text-transform: uppercase;
  }
  .address-line.first { left: 767px; top: 584px; }
  .address-line.second { left: 746px; top: 606px; }
</style>
</head>
<body>
<main class="stage">
  <svg class="card-shapes" width="1200" height="900" viewBox="0 0 1200 900" aria-hidden="true">
    <g class="card back-card">
      <path fill="var(--card-border)" d="M62,368 Q400,322 738,368 V808 Q400,852 62,808 Z"/>
      <path fill="var(--card-stock)" d="M90,394 Q400,354 710,394 V786 Q400,824 90,786 Z"/>
      <rect x="240" y="566" width="14" height="14" fill="var(--ink-navy)"/>
      <line x1="256" y1="613" x2="542" y2="613" stroke="var(--ink-navy)" stroke-width="0.8"/>
    </g>

    <g class="card front-card">
      <path fill="var(--card-border)" d="M642,52 Q868,38 1094,52 Q1114,386 1094,720 Q868,734 642,720 Q620,386 642,52 Z"/>
      <path fill="var(--card-stock)" d="M668,80 Q868,68 1068,80 Q1086,386 1068,696 Q868,708 668,696 Q648,386 668,80 Z"/>

      <g class="rules" stroke="var(--rule-green)" stroke-width="1.4">
        <line x1="733" y1="202" x2="1012" y2="202"/>
        <line x1="735" y1="360" x2="1013" y2="360"/>
        <line x1="735" y1="366" x2="1013" y2="366"/>
        <line x1="735" y1="440" x2="1013" y2="440"/>
        <line x1="735" y1="475" x2="1013" y2="475"/>
        <line x1="735" y1="530" x2="1013" y2="530"/>
        <line x1="735" y1="568" x2="1013" y2="568"/>
        <line x1="735" y1="632" x2="1013" y2="632"/>
        <line x1="735" y1="638" x2="1013" y2="638"/>
      </g>

      <g class="icon-phone" fill="var(--ink-navy)">
        <path d="M736,396 Q736,378 760,378 Q784,378 784,396 L774,398 L772,390 Q760,386 748,390 L746,398 Z"/>
        <path d="M744,400 L776,400 L782,426 L738,426 Z"/>
        <circle cx="760" cy="411" r="8" fill="var(--card-stock)"/>
        <circle cx="760" cy="411" r="4"/>
      </g>

      <g class="icon-globe" fill="none" stroke="var(--ink-navy)" stroke-width="1.6">
        <circle cx="745" cy="456" r="7.5" fill="var(--ink-navy)"/>
        <path d="M738,456 H752 M745,448.5 Q740,456 745,463.5 M745,448.5 Q750,456 745,463.5" stroke="var(--card-stock)" stroke-width="1"/>
      </g>

      <circle class="social-dot" cx="758" cy="501" r="13" fill="var(--ink-navy)"/>

      <g class="icon-pin" fill="var(--ink-navy)">
        <path d="M742,582 a7,7 0 0 1 7,7 c0,6 -7,13 -7,13 c0,0 -7,-7 -7,-13 a7,7 0 0 1 7,-7 Z"/>
        <circle cx="742" cy="589" r="2.6" fill="var(--card-stock)"/>
      </g>
    </g>
  </svg>

  <p class="text brand-name">BRIGHTWELL LEDGER</p>
  <p class="text brand-url">brightwellledger.com.au</p>

  <h1 class="text person-name">DORIAN FALKWELL</h1>
  <p class="text person-role">Consultant &amp; Educator</p>
  <p class="text phone-number">555.318.2947</p>
  <p class="text website">www.thegrantpathdesk.org</p>
  <p class="text social-handle">@TheGrantDesk</p>
  <p class="text email">dorian@thegrantpathdesk.org</p>
  <p class="text address-line first">1780 W. Harlowe Blvd</p>
  <p class="text address-line second">Suite C, Marlow, CA 93122</p>
</main>
</body>
</html>
```